Post Card (5x7) - Pre-foreclosure Image - Harbor Path Partners

(Two-Sided Post Card)
FACING FORECLOSURE? YOU STILL HAVE OPTIONS.
If you’re behind on payments or at risk of foreclosure, you’re not alone—and it’s not too late to take action.
We help homeowners:
• Explore options to stay in their home
• Stop or delay foreclosure
• Sell quickly for a fair price if needed
No pressure. No obligation. Just real solutions tailored to your situation.
Call - (240) 558-2094
Email - marcus@hpbllc-mail.com
Harbor Path Partners LLC
7200 Bramwick Lane, Ellicott City, MD 21043
**Marcus Fennimore is a Licensed Realtor with Copperleaf Homes Realty in Bethesda, Maryland.
(Leave room for mailing address, return address & postage)
Target Market(s)
Distressed Homeowners
Industry/Entity Type
Real Estate

```html
<!DOCTYPE html>
<html lang="en">
<head>
<meta charset="UTF-8">
<title>Harbor Path Partners – Pre-foreclosure Post Card</title>
<link href="https://fonts.googleapis.com/css2?family=Inter:wght@400;500;600;700;800&family=Inter+Tight:wght@400;500&display=swap" rel="stylesheet">
<style>
  :root {
    --bg: #d3d3d3;
    --paper: #ffffff;
    --ink: #0a0a0a;
    --muted: #8a8a8a;
    --band: #000000;
    --logo-box: #0d0d0e;
    --photo-top: #1c2433;
    --photo-bottom: #0f1522;
    --white: #ffffff;
  }
  * { margin: 0; padding: 0; box-sizing: border-box; }
  html, body { width: 862px; height: 1200px; overflow: hidden; }
  body {
    background: var(--bg);
    font-family: "Inter", Arial, sans-serif;
    position: relative;
  }
  .card {
    position: absolute;
    left: 91px;
    width: 681px;
    height: 486px;
    background: var(--paper);
    overflow: hidden;
  }
  .card--front { top: 94px; }
  .card--back { top: 619px; }

  /* Front */
  .headline {
    position: absolute; left: 31px; top: 44px;
    font-size: 39px; font-weight: 800; letter-spacing: -1.2px;
    color: var(--ink); white-space: nowrap;
  }
  .subhead {
    position: absolute; left: 31px; top: 96px;
    font-size: 25px; font-weight: 700; letter-spacing: -0.6px;
    color: var(--ink); white-space: nowrap;
  }
  .body-copy {
    font-family: "Inter Tight", "Inter", Arial, sans-serif;
    font-size: 14.2px; color: var(--muted); white-space: nowrap;
  }
  .intro {
    position: absolute; left: 31px; top: 151px;
    line-height: 23px;
  }
  .help-lead {
    position: absolute; left: 31px; top: 203px;
  }
  .help-list {
    position: absolute; left: 31px; top: 225px; list-style: none;
  }
  .help-list li {
    display: flex; align-items: center; gap: 8px;
    height: 23px;
  }
  .help-list svg { width: 14px; height: 14px; flex: none; }
  .reassure {
    position: absolute; left: 31px; top: 314px;
    font-size: 16.5px; line-height: 26px; font-weight: 500;
    letter-spacing: -0.2px; color: var(--ink); white-space: nowrap;
  }
  .call-band {
    position: absolute; left: 0; right: 0; top: 389px; height: 97px;
    background: var(--band);
  }
  .call-number {
    position: absolute; left: 31px; top: 416px;
    font-size: 33px; font-weight: 700; letter-spacing: -0.8px;
    color: var(--white); white-space: nowrap;
  }
  .agent-photo {
    position: absolute; left: 400px; top: 33px; width: 281px; height: 453px;
    background: linear-gradient(180deg, var(--photo-top), var(--photo-bottom));
    border-radius: 120px 0 0 0;
  }
  .agent {
    position: absolute; right: 31px; top: 412px; text-align: right; color: var(--white);
    white-space: nowrap;
  }
  .agent-name { font-size: 21px; font-weight: 700; letter-spacing: 0.2px; line-height: 24px; }
  .agent-title { font-size: 14px; font-weight: 400; line-height: 17px; }

  /* Back */
  .back-panel {
    position: absolute; left: 0; top: 0; width: 324px; height: 486px;
    background: var(--band);
  }
  .brand {
    position: absolute; left: 56px; top: 42px; width: 212px; height: 106px;
    background: var(--logo-box);
    display: flex; align-items: center; justify-content: center; gap: 7px;
  }
  .brand-mark { width: 9px; height: 9px; background: var(--white); flex: none; }
  .brand-name {
    font-size: 12px; font-weight: 600; letter-spacing: 1px;
    color: var(--white); text-transform: uppercase; white-space: nowrap;
  }
  .contact {
    position: absolute; left: 0; width: 324px; top: 383px;
    text-align: center; color: var(--white); font-size: 12px; line-height: 16.5px;
    white-space: nowrap;
  }
  .contact .company { font-weight: 600; margin-top: 4px; }
  .stamp-box {
    position: absolute; left: 587px; top: 25px; width: 70px; height: 88px;
    border: 1.5px solid var(--ink);
  }
  .address-lines { position: absolute; left: 355px; top: 187px; width: 302px; }
  .address-lines span {
    display: block; height: 1.5px; background: var(--ink); margin-bottom: 34.5px;
  }
</style>
</head>
<body>
  <section class="card card--front">
    <h1 class="headline">Facing Foreclosure?</h1>
    <h2 class="subhead">You Still Have Options</h2>
    <p class="intro body-copy">If you’re behind on payments or at risk of foreclosure,<br>you’re not alone, and it’s not too late to take action.</p>
    <p class="help-lead body-copy">We help homeowners:</p>
    <ul class="help-list body-copy">
      <li><svg viewBox="0 0 14 14"><path d="M1.5 7.5 L5 11 L12.5 3" fill="none" stroke="#0a0a0a" stroke-width="2.6"/></svg>Explore options to stay in their home</li>
      <li><svg viewBox="0 0 14 14"><path d="M1.5 7.5 L5 11 L12.5 3" fill="none" stroke="#0a0a0a" stroke-width="2.6"/></svg>Stop or delay foreclosure</li>
      <li><svg viewBox="0 0 14 14"><path d="M1.5 7.5 L5 11 L12.5 3" fill="none" stroke="#0a0a0a" stroke-width="2.6"/></svg>Sell quickly for a fair price if needed</li>
    </ul>
    <p class="reassure">No pressure. No obligation.<br>Just real solutions tailored to your situation.</p>
    <div class="call-band"></div>
    <p class="call-number">Call: (240) 558-2094</p>
    <div class="agent-photo" role="img" aria-label="Portrait photo of the realtor in a dark hat and navy jacket"></div>
    <div class="agent">
      <p class="agent-name">Marcus Fennimore</p>
      <p class="agent-title">Licensed Realtor</p>
    </div>
  </section>

  <section class="card card--back">
    <div class="back-panel">
      <div class="brand">
        <span class="brand-mark"></span>
        <span class="brand-name">Harbor Path Partners</span>
      </div>
      <div class="contact">
        <p>T: (240) 558-2094</p>
        <p>E: marcus@hpbllc-mail.com</p>
        <p class="company">Harbor Path Partners LLC</p>
        <p>7200 Bramwick Lane, Ellicott City, MD 21043</p>
      </div>
    </div>
    <div class="stamp-box"></div>
    <div class="address-lines"><span></span><span></span><span></span><span></span><span></span></div>
  </section>
</body>
</html>
```